Vitamin and Nutrition Ecommerce Site Needs a High End Website Design

We need a new and improved Homepage design for a leading Vitamin eCommerce business.
We supply our customers worldwide with leading brands of vitamin supplements and nutritional products at discounted prices.
The site design and layout must improve sales conversion and maximize the user experience staying on the site!

We will need to see;
A New Nutri Harbour stylized font (no logo)
High-End Modern Design
Easy Sales Conversion Experience
Excellent Layout, Fast Navigation
Quality Font style, Stylish Colour Palette Selection
Appropriate Spacing
Call To Action to Improve Sales Conversion
Web page should Look Clean and Minimalist

The design should improve sales, communicate easy to find products, facilitate fast ordering, have a modern and professional appearance centered toward a predominately female consumer.

Thank you for your interest in this project!

Current design can be found on this link;
www.nutriharbour.com.au/nutri/

Target Market(s)

80% Female 30-65 years

Industry/Entity Type

Business

Number of Pages Required

1 page

Colors

Designer to choose colors to be used in the design.

Requirements
Must have
• design must result improve sales conversion
• new Nutri Harbour font design
• search field
• attractive clean modern design
• stylish font and colour palette selection
Nice to have
• white background
Should not have
• cluttered or busy layout
• confusing navigation

```html
<!DOCTYPE html>
<html lang="en">
<head>
<meta charset="utf-8">
<title>Nutri Harbour — Home</title>
<link href="https://fonts.googleapis.com/css2?family=Questrial&family=Dancing+Script:wght@500;700&display=swap" rel="stylesheet">
<style>
:root{
  --mint:#7fb59b;
  --mint-dark:#5f9a80;
  --mint-pale:#e3efe8;
  --pink:#d9849c;
  --pink-pale:#f7e6eb;
  --grey-bg:#ececec;
  --ink:#444;
  --ink-soft:#888;
  --white:#fff;
  --maroon:#6a2c3b;
  --line:#dcdcdc;
}
*{box-sizing:border-box;margin:0;padding:0}
html,body{width:1200px;height:4108px;overflow:hidden}
body{font-family:"Questrial",Arial,sans-serif;color:var(--ink);background:var(--white);position:relative}
.abs{position:absolute}
.script{font-family:"Dancing Script",cursive}
.ph{position:absolute}

/* header */
.header{top:0;left:0;width:1200px;height:112px}
.logo{display:flex;align-items:center;gap:10px;color:var(--mint-dark);font-size:30px}
.logo .dot{width:18px;height:18px;border-radius:50%;background:var(--mint)}
.header .logo{position:absolute;left:80px;top:36px}
.search{position:absolute;left:836px;top:42px;width:170px;height:28px;border:1px solid var(--line);border-radius:14px;font-size:12px;color:var(--ink-soft);padding:6px 14px}
.header-icons{position:absolute;left:1030px;top:44px;display:flex;gap:14px}
.nav{top:112px;left:0;width:1200px;height:34px;background:var(--mint);display:flex;justify-content:center;gap:30px;align-items:center;font-size:11px;color:var(--white);letter-spacing:.5px}

/* hero */
.hero{top:146px;left:0;width:1200px;height:620px;background:linear-gradient(90deg,#f7faf8 0%,#eef5f0 55%,#e8f1ec 100%)}
.hero-visual{left:520px;top:30px;width:680px;height:590px;background:radial-gradient(ellipse at 60% 55%,#f2ead8 0%,#dfeee3 55%,rgba(232,241,236,0) 80%)}
.hero-text{left:80px;top:180px;width:400px}
.hero-text .eyebrow{font-size:26px;color:var(--mint-dark);letter-spacing:2px}
.hero-text .title{font-size:64px;color:#5a5a5a;line-height:1.1;margin:4px 0 18px}
.hero-text p{font-size:13px;line-height:1.6;color:var(--ink-soft)}
.btn-outline{display:inline-block;margin-top:26px;border:1px solid #666;border-radius:3px;padding:11px 20px;font-size:12px;color:#555}

/* features */
.feature{top:790px;width:212px;height:70px;background:#d99aab;color:var(--white);display:flex;align-items:center;gap:12px;padding:0 16px}
.feature b{display:block;font-weight:normal;font-size:12px;letter-spacing:1px}
.feature span{font-size:10px;opacity:.9}

.section-title{position:absolute;left:0;width:1200px;text-align:center;font-size:34px;color:#4d4d4d;letter-spacing:1px;z-index:2}
.section-sub{position:absolute;left:0;width:1200px;text-align:center;font-size:22px;color:var(--ink-soft);z-index:2}

/* offers */
.offer{top:1022px;width:500px;height:228px;overflow:hidden}
.offer .copy{position:absolute;top:60px;color:var(--white)}
.offer .pct{font-size:26px}
.offer .name{font-size:44px;line-height:1}
.offer p{font-size:11px;width:190px;margin-top:8px;line-height:1.5}
.offer .btn-sm{display:inline-block;margin-top:12px;padding:5px 12px;font-size:10px;border-radius:12px;background:rgba(0,0,0,.35);color:#fff}

/* latest */
.latest{top:1288px;left:0;width:1200px;height:735px;background:var(--grey-bg)}
.tabs{position:absolute;top:1500px;left:0;width:1200px;display:flex;justify-content:center;gap:14px}
.tab{width:120px;height:38px;line-height:38px;text-align:center;font-size:12px;border-radius:3px;background:#f3d4dd;color:#666}
.tab.active{background:var(--pink);color:#fff}
.card{top:1608px;width:220px;height:372px;background:var(--white);box-shadow:0 2px 6px rgba(0,0,0,.08)}
.card .thumb{left:55px;top:34px;width:110px;height:150px}
.card .tag{position:absolute;right:0;top:0;background:var(--mint);color:#fff;font-size:9px;padding:3px 8px}
.card .info{position:absolute;top:206px;left:0;width:220px;text-align:center;font-size:12px;line-height:1.5}
.price{font-size:12px}
.price s{color:var(--ink-soft)}
.stars{color:var(--mint-dark);font-size:12px;letter-spacing:2px}
.btn-cart{display:inline-block;margin-top:10px;border:1px solid #bbb;border-radius:14px;padding:5px 14px;font-size:10px;color:#555}
.arrow{top:1780px;font-size:28px;color:#777}

/* brands */
.brands{top:2048px;left:0;width:1200px;height:134px;background:var(--mint)}
.brand{top:2086px;width:190px;height:58px;background:var(--white);display:flex;align-items:center;justify-content:center;font-size:22px;color:#333}

/* recommended */
.recommend{top:2208px;left:0;width:1200px;height:592px;background:linear-gradient(180deg,#fbeef1 0%,var(--pink-pale) 100%)}
.flora{border-radius:50%;background:radial-gradient(circle,#f2b6a9 0%,rgba(247,230,235,0) 70%)}
.rec-box{background:var(--white);box-shadow:0 2px 6px rgba(0,0,0,.06)}
.rec-box .small{font-size:11px;color:var(--ink-soft);line-height:1.5}

/* columns */
.col-title{top:2902px;font-size:24px;color:#4d4d4d}
.mini{display:flex;gap:16px;align-items:center;width:300px}
.mini .t{width:60px;height:70px;border:1px solid var(--line);position:relative}
.mini .t i{position:absolute;left:20px;top:12px;width:22px;height:46px;border-radius:4px}
.mini p{font-size:12px;line-height:1.5;color:#666}

/* testimonial & rewards */
.testi{top:3312px;left:0;width:640px;height:448px;background:linear-gradient(135deg,#3e3f3c 0%,#5c5e57 60%,#4a4b47 100%)}
.avatar{top:3384px;left:276px;width:88px;height:88px;border-radius:50%;background:#c9b7a2;border:4px solid #fff}
.rewards{top:3312px;left:640px;width:560px;height:448px;background:linear-gradient(180deg,#eef5f1,#dfece4)}

/* footer */
.footer-col h4{font-weight:normal;font-size:14px;color:#444;margin-bottom:14px}
.footer-col li{list-style:none;font-size:12px;color:#777;margin-bottom:10px}
.footer-col li::before{content:"›";margin-right:8px;color:var(--mint-dark)}
.bottom{top:4048px;left:0;width:1200px;height:60px;background:var(--maroon);color:#e8cfd5;font-size:12px;text-align:center;line-height:60px}
</style>
</head>
<body>

<header class="abs header">
  <div class="logo"><span class="dot"></span>Nutri Harbour</div>
  <div class="search">Search…</div>
  <div class="header-icons">
    <svg width="16" height="16" viewBox="0 0 16 16"><circle cx="8" cy="5" r="3.5" fill="none" stroke="#666" stroke-width="1.4"/><path d="M1.5 15c0-3.5 3-5.5 6.5-5.5s6.5 2 6.5 5.5" fill="none" stroke="#666" stroke-width="1.4"/></svg>
    <svg width="16" height="16" viewBox="0 0 16 16"><path d="M8 14S1.5 10 1.5 5.5A3.3 3.3 0 0 1 8 4a3.3 3.3 0 0 1 6.5 1.5C14.5 10 8 14 8 14z" fill="none" stroke="#666" stroke-width="1.4"/></svg>
    <svg width="18" height="16" viewBox="0 0 18 16"><path d="M1 1h3l2 9h9l2-7H5" fill="none" stroke="#666" stroke-width="1.4"/><circle cx="7" cy="13.5" r="1.4" fill="#666"/><circle cx="14" cy="13.5" r="1.4" fill="#666"/></svg>
  </div>
</header>

<nav class="abs nav">
  <span>HOME</span><span>BRANDS</span><span>SUPPLEMENTS</span><span>SPORTS NUTRITION</span><span>SKINCARE</span><span>CORPORATE WELLNESS</span><span>HEALTH CONDITIONS</span><span>BEAUTY &amp; SKINCARE</span><span>GLUTEN FREE</span><span>ON SALE</span>
</nav>

<section class="abs hero">
  <div class="ph hero-visual" role="img" aria-label="Group of vitamin bottles with a milk splash and green leaves"></div>
  <div class="abs hero-text">
    <div class="eyebrow">WELCOME TO</div>
    <div class="title script">Nutri Harbour !</div>
    <p>With savings of up to 70% off Recommended Retail Prices we invite you to browse our shop with us at Nutri Harbour. Here you will find we are a leading Australian health retailer specialising in Professional, fast and reliable service for all your natural healthcare needs.</p>
    <span class="btn-outline">GET FREE PROMO CODE</span>
  </div>
</section>

<div class="abs feature" style="left:80px">
  <svg width="28" height="22" viewBox="0 0 28 22"><path d="M1 3h16v12H1zM17 7h6l4 4v4h-10z" fill="none" stroke="#fff" stroke-width="1.6"/><circle cx="6" cy="17" r="2.5" fill="#fff"/><circle cx="22" cy="17" r="2.5" fill="#fff"/></svg>
  <div><b>FREE SHIPPING</b><span>On orders over $99</span></div>
</div>
<div class="abs feature" style="left:336px">
  <svg width="24" height="24" viewBox="0 0 24 24"><rect x="2" y="8" width="20" height="14" fill="none" stroke="#fff" stroke-width="1.6"/><path d="M2 8h20M12 8v14M12 8C8 2 4 4 7 8M12 8c4-6 8-4 5 0" fill="none" stroke="#fff" stroke-width="1.6"/></svg>
  <div><b>SPECIAL OFFERS</b><span>Deals updated every week</span></div>
</div>
<div class="abs feature" style="left:592px">
  <svg width="24" height="24" viewBox="0 0 24 24"><path d="M12 2l8 3v7c0 5-4 8-8 10-4-2-8-5-8-10V5z" fill="none" stroke="#fff" stroke-width="1.6"/><path d="M8 12l3 3 5-6" fill="none" stroke="#fff" stroke-width="1.6"/></svg>
  <div><b>CYBER GUARDED</b><span>Secure online checkout</span></div>
</div>
<div class="abs feature" style="left:848px">
  <svg width="24" height="24" viewBox="0 0 24 24"><circle cx="12" cy="12" r="10" fill="none" stroke="#fff" stroke-width="1.6"/><path d="M12 6v6l4 3" fill="none" stroke="#fff" stroke-width="1.6"/></svg>
  <div><b>QUICK DISPATCH</b><span>Same day before 2pm</span></div>
</div>

<h2 class="section-title" style="top:940px">SPECIAL OFFERS</h2>

<div class="abs offer" style="left:80px;background:linear-gradient(90deg,#e9c8b6 0%,#c79c84 45%,#a7c08a 100%)" role="img" aria-label="Skin care banner with woman touching her face">
  <div class="copy" style="left:290px">
    <div class="pct">20% OFF</div>
    <div class="name script">Skin Care</div>
    <p>Lorem Ipsum is simply dummy text of the printing and typesetting industry.</p>
    <span class="btn-sm">SHOP NOW</span>
  </div>
</div>
<div class="abs offer" style="left:620px;background:linear-gradient(90deg,#b98a5e 0%,#6d7f7c 45%,#2f6f78 100%)" role="img" aria-label="Hair care banner with woman with flowing hair">
  <div class="copy" style="left:290px">
    <div class="pct">30% OFF</div>
    <div class="name script">Hair Care</div>
    <p>Lorem Ipsum is simply dummy text of the printing and typesetting industry.</p>
    <span class="btn-sm">SHOP NOW</span>
  </div>
</div>

<section class="abs latest"></section>
<div class="ph" style="left:0;top:1288px;width:260px;height:260px;background:radial-gradient(circle at 30% 30%,#d2d2d2,rgba(236,236,236,0) 70%)" role="img" aria-label="Line drawing of tropical leaves"></div>
<div class="ph" style="left:1060px;top:1640px;width:140px;height:380px;background:radial-gradient(ellipse at 80% 50%,#86b07f,rgba(236,236,236,0) 70%)" role="img" aria-label="Green palm leaves"></div>
<h2 class="section-title" style="top:1380px">LATEST PRODUCTS</h2>
<div class="section-sub script" style="top:1430px">For every user at the forefront of creation</div>
<div class="tabs"><span class="tab active">ALL</span><span class="tab">SKIN CARE</span><span class="tab">HAIR CARE</span></div>

<div class="abs arrow" style="left:30px">‹</div>
<div class="abs arrow" style="left:1150px">›</div>

<div class="abs card" style="left:80px"><span class="tag">NEW</span>
  <div class="ph thumb" style="background:linear-gradient(180deg,#f1f1f1,#dde6ee)" role="img" aria-label="White supplement bottle with blue label"></div>
  <div class="info">Serenity Pillow<br>Standard Bed Super Soft Density<br><span class="price"><s>$15.99</s> | $12.99</span><br><span class="stars">★★★★★</span><br><span class="btn-cart">ADD TO CART</span></div>
</div>
<div class="abs card" style="left:348px">
  <div class="ph thumb" style="background:linear-gradient(180deg,#f6f6f6,#e4e4e4)" role="img" aria-label="White supplement tub"></div>
  <div class="info">Serenity Pillow<br>Standard Bed Super Soft Density<br><span class="price"><s>$15.99</s> | $12.99</span><br><span class="stars">★★★★★</span><br><span class="btn-cart">ADD TO CART</span></div>
</div>
<div class="abs card" style="left:612px"><span class="tag">NEW</span>
  <div class="ph thumb" style="background:linear-gradient(180deg,#8a4a22,#3a1d10)" role="img" aria-label="Amber supplement bottle"></div>
  <div class="info">Serenity Pillow<br>Standard Bed Super Soft Density<br><span class="price"><s>$15.99</s> | $12.99</span><br><span class="stars">★★★★★</span><br><span class="btn-cart">ADD TO CART</span></div>
</div>
<div class="abs card" style="left:876px"><span class="tag">NEW</span>
  <div class="ph thumb" style="background:linear-gradient(180deg,#2f2f2f,#4e7a3a)" role="img" aria-label="Dark supplement tub with green label"></div>
  <div class="info">Serenity Pillow<br>Standard Bed Super Soft Density<br><span class="price"><s>$15.99</s> | $12.99</span><br><span class="stars">★★★★★</span><br><span class="btn-cart">ADD TO CART</span></div>
</div>

<section class="abs brands"></section>
<div class="abs brand" style="left:100px">Evora</div>
<div class="abs brand" style="left:360px">Dermique</div>
<div class="abs brand" style="left:628px">Lustrelle</div>
<div class="abs brand" style="left:888px">Claridy</div>

<section class="abs recommend"></section>
<div class="ph flora" style="left:-40px;top:2200px;width:300px;height:240px" role="img" aria-label="Watercolour flowers"></div>
<div class="ph flora" style="left:940px;top:2640px;width:300px;height:200px;background:radial-gradient(circle,#e6c9d6 0%,rgba(247,230,235,0) 70%)" role="img" aria-label="Watercolour flowers"></div>
<h2 class="section-title" style="top:2262px">RECOMMENDED FOR YOU</h2>
<div class="section-sub script" style="top:2314px">For every user at the forefront of creation</div>

<div class="abs rec-box" style="left:80px;top:2428px;width:500px;height:332px">
  <div class="ph" style="left:30px;top:60px;width:200px;height:200px;background:linear-gradient(180deg,#6a4320,#c08a4a)" role="img" aria-label="Three amber vitamin bottles"></div>
  <div class="abs" style="left:260px;top:70px;width:210px">
    <div class="script" style="font-size:32px;color:#444">Exclusive Offers</div>
    <div style="font-size:13px;margin:10px 0 6px">B-COMPLEX VITAMINS</div>
    <div class="small">Lorem Ipsum is simply dummy text of the printing and typesetting industry.</div>
    <div class="price" style="margin-top:12px"><s>$15.99</s> | $12.99</div>
    <span class="btn-cart">ADD TO CART</span>
  </div>
</div>
<div class="abs rec-box" style="left:612px;top:2428px;width:508px;height:156px">
  <div class="ph" style="left:30px;top:24px;width:80px;height:108px;background:linear-gradient(180deg,#2b2b2b,#7a4a20)" role="img" aria-label="Coffee bag"></div>
  <div class="abs" style="left:136px;top:26px;width:280px">
    <div style="font-size:13px">ARABICA BLEND</div>
    <div class="small">Lorem Ipsum is simply dummy text of the printing.</div>
    <div class="price" style="margin-top:6px"><s>$15.99</s> | $12.99</div>
    <span class="btn-cart">ADD TO CART</span>
  </div>
</div>
<div class="abs rec-box" style="left:612px;top:2604px;width:508px;height:156px">
  <div class="ph" style="left:30px;top:24px;width:80px;height:108px;background:linear-gradient(180deg,#e8e8e8,#c9d6de)" role="img" aria-label="Two white bottles"></div>
  <div class="abs" style="left:136px;top:26px;width:280px">
    <div style="font-size:13px">ARABICA BLEND</div>
    <div class="small">Lorem Ipsum is simply dummy text of the printing.</div>
    <div class="price" style="margin-top:6px"><s>$15.99</s> | $12.99</div>
    <span class="btn-cart">ADD TO CART</span>
  </div>
</div>

<div class="ph" style="left:0;top:2800px;width:1200px;height:120px;background:radial-gradient(ellipse at 15% 20%,#f4dbe4,rgba(255,255,255,0) 45%)" role="img" aria-label="Soft pink watercolour wash"></div>
<div class="abs col-title" style="left:80px">BEST SELLERS</div>
<div class="abs col-title" style="left:460px">POPULAR PRODUCTS</div>
<div class="abs col-title" style="left:820px">NEW ARRIVAL</div>

<div class="abs" style="left:80px;top:2960px;display:flex;flex-direction:column;gap:20px">
  <div class="mini"><div class="t"><i style="background:#cfd8de"></i></div><p>Lorem Ipsum is simply<br>dummy text of the<br><s>$15.99</s> | $12.99</p></div>
  <div class="mini"><div class="t"><i style="background:#7a4520"></i></div><p>Lorem Ipsum is simply<br>dummy text of the<br><s>$15.99</s> | $12.99</p></div>
  <div class="mini"><div class="t"><i style="background:#3a3a3a"></i></div><p>Lorem Ipsum is simply<br>dummy text of the<br><s>$15.99</s> | $12.99</p></div>
</div>
<div class="abs" style="left:460px;top:2960px;display:flex;flex-direction:column;gap:20px">
  <div class="mini"><div class="t"><i style="background:#8a5a2a"></i></div><p>Lorem Ipsum is simply<br>dummy text of the<br><s>$15.99</s> | $12.99</p></div>
  <div class="mini"><div class="t"><i style="background:#d8d8d8"></i></div><p>Lorem Ipsum is simply<br>dummy text of the<br><s>$15.99</s> | $12.99</p></div>
  <div class="mini"><div class="t"><i style="background:#6b3c1c"></i></div><p>Lorem Ipsum is simply<br>dummy text of the<br><s>$15.99</s> | $12.99</p></div>
</div>
<div class="abs" style="left:820px;top:2960px;display:flex;flex-direction:column;gap:20px">
  <div class="mini"><div class="t"><i style="background:#d2dde4"></i></div><p>Lorem Ipsum is simply<br>dummy text of the<br><s>$15.99</s> | $12.99</p></div>
  <div class="mini"><div class="t"><i style="background:#7a4520"></i></div><p>Lorem Ipsum is simply<br>dummy text of the<br><s>$15.99</s> | $12.99</p></div>
  <div class="mini"><div class="t"><i style="background:#2f2f2f"></i></div><p>Lorem Ipsum is simply<br>dummy text of the<br><s>$15.99</s> | $12.99</p></div>
</div>

<section class="abs testi" role="img" aria-label="Dimmed lifestyle photo behind customer testimonial"></section>
<div class="abs avatar" role="img" aria-label="Customer portrait"></div>
<div class="abs" style="left:0;top:3488px;width:640px;text-align:center;color:#fff">
  <div style="font-size:16px">JOHN DOE</div>
  <div style="font-size:11px;opacity:.8;margin-top:4px">Customer</div>
  <p style="width:440px;margin:22px auto 0;font-size:13px;line-height:1.7;opacity:.9">"It is a long established fact that a reader will be distracted by the readable content of a page when looking at its layout. The point of using Lorem Ipsum is that it has a more-or-less normal distribution of letters."</p>
  <div style="margin-top:26px;display:flex;gap:8px;justify-content:center">
    <span style="width:8px;height:8px;border-radius:50%;background:#fff"></span>
    <span style="width:8px;height:8px;border-radius:50%;background:rgba(255,255,255,.45)"></span>
    <span style="width:8px;height:8px;border-radius:50%;background:rgba(255,255,255,.45)"></span>
  </div>
</div>

<section class="abs rewards"></section>
<div class="ph" style="left:1060px;top:3312px;width:140px;height:150px;background:radial-gradient(circle at 80% 20%,#9cc59b,rgba(223,236,228,0) 70%)" role="img" aria-label="Green leaves"></div>
<div class="abs" style="left:680px;top:3380px;width:440px">
  <div style="font-size:26px;color:#4d4d4d">JOIN NUTRI HARBOUR REWARDS</div>
  <p style="font-size:13px;color:#777;line-height:1.6;margin-top:16px">Be rewarded with exclusive member offers, including discounts, sales, freebies, gifts with purchase and competitions.</p>
  <div style="margin-top:40px;width:320px;height:42px;border:1px solid #bcd2c5;background:#fff;font-size:12px;color:#999;padding:13px 16px">Enter your email…</div>
  <div style="margin-top:16px;width:320px;height:44px;background:var(--mint);color:#fff;text-align:center;line-height:44px;font-size:13px;letter-spacing:1px">SUBSCRIBE</div>
</div>

<footer>
  <div class="abs" style="left:80px;top:3810px">
    <div class="logo"><span class="dot"></span>Nutri Harbour</div>
    <div style="margin-top:30px;font-size:13px;color:#666;display:flex;align-items:center;gap:8px">
      <svg width="14" height="14" viewBox="0 0 14 14"><path d="M3 1l2 3-1.5 1.5a8 8 0 0 0 5 5L10 9l3 2-1.5 2.5C6 13 1 8 .5 2.5z" fill="var(--mint-dark)"/></svg>1300 555 019
    </div>
  </div>
  <div class="abs footer-col" style="left:560px;top:3810px"><h4>Quick Links</h4><ul><li>About Us</li><li>Customer Service</li><li>Privacy Policy</li></ul></div>
  <div class="abs footer-col" style="left:780px;top:3810px"><h4>Products</h4><ul><li>About Us</li><li>Customer Service</li><li>Privacy Policy</li></ul></div>
  <div class="abs footer-col" style="left:990px;top:3810px"><h4>Mobile app</h4>
    <div style="width:120px;height:34px;background:#d8d8d8;border-radius:4px"></div>
    <div style="width:120px;height:34px;background:#e6e6e6;border-radius:4px;margin-top:10px"></div>
  </div>
</footer>
<div class="abs bottom">www.nutriharbour.com.au/nutri/ © 2017 All rights reserved</div>

</body>
</html>
```